Food manufacturer stationary
Business cards, envelopes, letterhead, cover sheet etc
Professional
Gustavo Arrieta
CEO
2875 North Clover Ave Cedar Vale, UT 84117
GUSTAVOJR@CORVANAFOODS.EXAMPLE
WWW.CORVANAMEXICANFOODS.EXAMPLE
Looking for something classy, professional, and modern. Something that says to client holding card this is a well established strong company

```html
<!DOCTYPE html>
<html lang="en">
<head>
<meta charset="utf-8">
<title>Corvana Mexican Foods Stationery</title>
<link href="https://fonts.googleapis.com/css2?family=Cinzel:wght@600&family=Lato:wght@400;700&display=swap" rel="stylesheet">
<style>
:root{
  --bg:#e9dcc4;
  --paper:#ffffff;
  --brown:#3d2410;
  --gold:#c9a35c;
  --gold-light:#e6cf98;
  --ink:#3a3027;
  --muted:#8a7a68;
  --faint:#f1ebe1;
}
*{box-sizing:border-box;margin:0;padding:0}
html,body{width:1200px;height:317px;overflow:hidden;background:var(--bg)}
body{position:relative;font-family:'Lato',sans-serif;color:var(--ink)}
.item{position:absolute}
.tiny{position:absolute;transform:scale(.5);transform-origin:top left;white-space:nowrap}
.tiny.right{transform-origin:top right;text-align:right}
.tiny.center{transform-origin:top center;text-align:center}
.label{position:absolute;font-size:10px;color:var(--muted);white-space:nowrap;left:50%;top:100%;margin-top:2px;transform:translateX(-50%) scale(.5);transform-origin:top center}
.brand{position:absolute;display:flex;align-items:center;gap:3px;font-family:'Cinzel',serif;font-weight:600;color:var(--gold);letter-spacing:.05em;white-space:nowrap}
.brand .dot{width:7px;height:7px;border-radius:50%;background:var(--gold)}
.brand-plate{background:var(--brown);padding:3px 6px;border-radius:2px}

/* business cards */
.card{width:84px;height:48px;box-shadow:0 1px 2px rgba(0,0,0,.25)}
.card.light{background:var(--paper)}
.card.dark{background:var(--brown)}
.card .brand{font-size:5px;left:6px;top:8px}
.card .brand .dot{width:5px;height:5px}
.card .info{left:6px;top:22px;font-size:6.4px;line-height:1.45;color:var(--ink)}
.card.dark .info{color:var(--gold-light)}
.card .name{font-weight:700;font-size:8px}
.card .art{position:absolute;left:4px;bottom:4px;width:26px;height:30px;border-radius:2px;background:linear-gradient(160deg,var(--gold-light),var(--gold))}

/* letterheads */
.letter{width:206px;height:276px;background:var(--paper);box-shadow:0 1px 3px rgba(0,0,0,.25);overflow:hidden}
.band{position:absolute;left:0;right:0;height:5px;background:linear-gradient(90deg,var(--brown),var(--gold),var(--brown))}
.band.top{top:0}.band.bottom{bottom:0}
.letter .brand{font-size:7px;left:20px;top:14px}
.letter .contact{right:18px;top:16px;font-size:7px;line-height:1.5;color:var(--muted)}
.watermark{position:absolute;left:50%;top:52%;width:110px;height:110px;margin:-55px 0 0 -55px;border-radius:50%;background:var(--faint);display:flex;align-items:center;justify-content:center;font-family:'Cinzel',serif;font-weight:600;font-size:12px;color:#e4d8c6;letter-spacing:.08em}

/* envelopes */
.envelope{width:209px;background:var(--paper);box-shadow:0 1px 3px rgba(0,0,0,.25);overflow:hidden}
.envelope .band{top:auto;bottom:0;height:4px}
.envelope .brand{font-size:5px;left:8px;top:6px}
.envelope .brand .dot{width:5px;height:5px}
.envelope .contact{left:9px;top:20px;font-size:6px;line-height:1.5;color:var(--muted)}
.envelope .watermark{width:54px;height:54px;margin:-27px 0 0 -27px;font-size:7px}

/* flap options */
.flap{width:300px;height:56px}
.flap .seal{position:absolute;left:50%;top:30px;width:12px;height:12px;margin-left:-6px;border-radius:50%;background:var(--brown);border:2px solid var(--gold)}
</style>
</head>
<body>

<div class="item card light" style="left:17px;top:108px">
  <div class="brand brand-plate" style="left:4px;top:6px"><span class="dot"></span>CORVANA</div>
  <div class="tiny info"><div class="name">Gustavo Arrieta</div>CEO<br>2875 North Clover Ave<br>Cedar Vale, UT 84117</div>
  <span class="label">Business Card Front</span>
</div>
<div class="item card dark" style="left:108px;top:108px">
  <div class="brand"><span class="dot"></span>CORVANA</div>
  <div class="tiny info">GUSTAVOJR@CORVANAFOODS.EXAMPLE<br>WWW.CORVANAMEXICANFOODS.EXAMPLE</div>
  <span class="label">Business Card Back</span>
</div>
<div class="item card light" style="left:17px;top:168px">
  <div class="art" role="img" aria-label="Gold illustration area"></div>
  <span class="label">Business Card Option</span>
</div>
<div class="item card dark" style="left:108px;top:168px">
  <div class="art" role="img" aria-label="Gold illustration area"></div>
  <div class="tiny info" style="left:36px;top:16px"><div class="name">Gustavo Arrieta</div>CEO</div>
  <span class="label">Business Card Option</span>
</div>

<div class="item letter" style="left:216px;top:19px">
  <div class="band top"></div>
  <div class="brand brand-plate"><span class="dot"></span>CORVANA</div>
  <div class="tiny right contact">2875 North Clover Ave<br>Cedar Vale, UT 84117<br>WWW.CORVANAMEXICANFOODS.EXAMPLE</div>
  <div class="watermark">CORVANA</div>
  <div class="band bottom"></div>
</div>
<span class="label" style="left:319px;top:295px">Letterhead Page 1</span>
<div class="item letter" style="left:439px;top:19px">
  <div class="band top"></div>
  <div class="brand brand-plate" style="left:50%;transform:translateX(-50%)"><span class="dot"></span>CORVANA</div>
  <div class="watermark">CORVANA</div>
  <div class="tiny center contact" style="right:auto;top:auto;left:0;width:206px;bottom:6px">2875 North Clover Ave, Cedar Vale, UT 84117</div>
  <div class="band bottom"></div>
</div>
<span class="label" style="left:542px;top:295px">Letterhead Page 2</span>

<div class="item envelope" style="left:667px;top:108px;height:60px">
  <div class="brand brand-plate"><span class="dot"></span>CORVANA</div>
  <div class="tiny contact">2875 North Clover Ave<br>Cedar Vale, UT 84117</div>
  <div class="band"></div>
</div>
<span class="label" style="left:771px;top:168px">Envelope Front</span>
<div class="item envelope" style="left:667px;top:180px;height:72px">
  <div class="brand brand-plate"><span class="dot"></span>CORVANA</div>
  <div class="watermark">CORVANA</div>
  <div class="band"></div>
</div>
<span class="label" style="left:771px;top:252px">Envelope Back</span>

<div class="item flap" style="left:888px;top:19px">
  <svg width="300" height="56" viewBox="0 0 300 56"><defs><linearGradient id="gold" x1="0" x2="1"><stop offset="0" stop-color="#a8843f"/><stop offset=".5" stop-color="#e6cf98"/><stop offset="1" stop-color="#a8843f"/></linearGradient></defs><rect width="300" height="56" fill="url(#gold)"/><path d="M0 0 L150 38 L300 0" fill="none" stroke="#8c6a2e" stroke-width="1"/></svg>
  <div class="seal"></div>
</div>
<div class="item flap" style="left:888px;top:94px">
  <svg width="300" height="56" viewBox="0 0 300 56"><defs><linearGradient id="silver" x1="0" x2="1"><stop offset="0" stop-color="#7d7d7d"/><stop offset=".5" stop-color="#dcdcdc"/><stop offset="1" stop-color="#7d7d7d"/></linearGradient></defs><rect width="300" height="56" fill="url(#silver)"/><path d="M0 0 L150 38 L300 0" fill="none" stroke="#6a6a6a" stroke-width="1"/></svg>
  <div class="seal"></div>
</div>
<div class="item flap" style="left:888px;top:168px;height:84px">
  <svg width="300" height="84" viewBox="0 0 300 84"><rect width="300" height="84" fill="#ffffff"/><path d="M0 0 L150 40 L300 0" fill="#f6f3ee" stroke="#cfc6b8" stroke-width="1"/><path d="M0 84 L150 44 L300 84" fill="none" stroke="#e3ddd3" stroke-width="1"/></svg>
  <div class="seal"></div>
</div>
<span class="label" style="left:1038px;top:254px">Envelope Color Options</span>

</body>
</html>
```